Australian Civil Construction, Quarry & Mining Services needs a business card

We need a business card designed for our Civil Construction, Quarry & Mining Services based in the country in Australia.
Our Company Brackley Earthworks provide innovate solutions for infrastructure, agricultural and mining (aggregate, sand, roadbase) industry.
We would like our business cards to be double sided
Front of card: black background or something that resembles our business colours. (it doesn't have to be black we are open to options)
- Company name - Brackley Earthworks
- Either our logo or some sort of icon/picture that resembles our business
- Website - https://brackleyearthworks.com.au/
- We will have a number of different names, positions descriptions, phone numbers and emails on separate cards for each of our managers/directors

```html
<!DOCTYPE html>
<html lang="en">
<head>
<meta charset="utf-8">
<title>Brackley Earthworks – Business Card</title>
<link rel="stylesheet" href="https://fonts.googleapis.com/css2?family=Montserrat:wght@400;700&display=swap">
<style>
  :root {
    --card-black: #0a0c0b;
    --orange: #f58220;
    --white: #ffffff;
    --backdrop: #e4e5e6;
    --pattern-light: #1c1c1c;
    --pattern-dark: #0c0c0c;
  }
  * { margin: 0; padding: 0; box-sizing: border-box; }
  html, body { width: 1200px; height: 1200px; overflow: hidden; }
  body {
    background: var(--backdrop);
    font-family: "Montserrat", sans-serif;
    position: relative;
  }
  .card {
    position: absolute;
    top: 453px;
    width: 516px;
    height: 294px;
    background: var(--card-black);
    color: var(--white);
    overflow: hidden;
  }
  .card--front { left: 57px; }
  .card--back { left: 632px; }

  .brand-name {
    position: absolute;
    left: 22px;
    top: 82px;
    width: 170px;
    font-weight: 700;
    font-size: 24px;
    line-height: 1.15;
    color: var(--orange);
  }
  .person-name {
    position: absolute;
    left: 22px;
    top: 222px;
    font-weight: 700;
    font-size: 23px;
    line-height: 28px;
    letter-spacing: 0.5px;
    white-space: nowrap;
  }
  .person-role {
    position: absolute;
    left: 22px;
    top: 250px;
    font-size: 13px;
    line-height: 16px;
    color: var(--orange);
  }
  .rule {
    position: absolute;
    left: 140px;
    top: 259px;
    width: 264px;
    height: 1px;
    background: var(--orange);
  }
  .contact-list {
    position: absolute;
    right: 43px;
    top: 156px;
    list-style: none;
    text-align: right;
    font-size: 12.8px;
    line-height: 18px;
    white-space: nowrap;
  }
  .contact-list li { position: relative; height: 18px; }
  .contact-phone { font-size: 16px; line-height: 22px; height: 22px !important; }
  .contact-web .accent { color: var(--orange); }
  .contact-address { margin-top: 2px; }
  .icon {
    position: absolute;
    right: -24px;
    top: 2px;
    width: 14px;
    height: 14px;
  }
  .contact-phone .icon { top: 4px; }

  .back-texture {
    position: absolute;
    inset: 0;
    background: linear-gradient(100deg, var(--pattern-light) 0%, #151515 50%, var(--pattern-dark) 100%);
  }
  .back-mark {
    position: absolute;
    left: 252px;
    top: 212px;
    width: 18px;
    height: 18px;
    background: var(--orange);
  }
  .back-name {
    position: absolute;
    left: 0;
    right: 0;
    top: 246px;
    text-align: center;
    font-weight: 700;
    font-size: 17px;
    line-height: 22px;
    letter-spacing: 0.3px;
  }
</style>
</head>
<body>
  <section class="card card--front">
    <div class="brand-name">Brackley Earthworks</div>

    <ul class="contact-list">
      <li class="contact-phone">03 5012 3486
        <svg class="icon" viewBox="0 0 16 16" fill="none" stroke="#f58220" stroke-width="1.4"><path d="M3 2l3 0 1 3.5-1.8 1.2a8 8 0 0 0 4.1 4.1L10.5 9 14 10v3a1 1 0 0 1-1 1A11 11 0 0 1 2 3a1 1 0 0 1 1-1z"/></svg>
      </li>
      <li class="contact-email">admin@brackleyearthworks.com.au
        <svg class="icon" viewBox="0 0 16 16" fill="none" stroke="#f58220" stroke-width="1.4"><rect x="1.5" y="3.5" width="13" height="9" rx="1"/><path d="M1.5 4l6.5 5 6.5-5"/></svg>
      </li>
      <li class="contact-web"><span class="accent">brackleyearthworks</span>.com.au
        <svg class="icon" viewBox="0 0 16 16" fill="none" stroke="#f58220" stroke-width="1.4"><circle cx="8" cy="8" r="6.5"/><path d="M1.5 8h13M8 1.5c-3 3.5-3 9.5 0 13M8 1.5c3 3.5 3 9.5 0 13"/></svg>
      </li>
      <li class="contact-address">14 Kestrel Lane
        <svg class="icon" viewBox="0 0 16 16" fill="none" stroke="#f58220" stroke-width="1.4"><path d="M8 15s5-5 5-8.5a5 5 0 0 0-10 0C3 10 8 15 8 15z"/><circle cx="8" cy="6.5" r="1.8"/></svg>
      </li>
      <li>Wattlebrook Victoria 3730</li>
      <li>Australia</li>
    </ul>

    <div class="person-name">LIAM CARTER</div>
    <div class="person-role">Project Manager</div>
    <div class="rule"></div>
  </section>

  <section class="card card--back">
    <div class="back-texture" role="img" aria-label="Subtle dark geometric background pattern"></div>
    <div class="back-mark"></div>
    <div class="back-name">BRACKLEY EARTHWORKS</div>
  </section>
</body>
</html>
```